Pharmacy handmade, Personalized Medical Cosmetics Label

Medical Cosmetics label, elegant and professional looking. The creams are Dermatologist formulated and are prepared by local Pharmacy. The label should be versatile and allow space for hand writing to be filled by the pharmacist preparing the product.
The following information will be handwritten:
Upper lid - Lid Balm No.5 ; Marigold, Retinol ; 30
Lower Bottom - Teodora Halvik ; Signature ; 01.01.2017
Upper Lid Label
Velluto Skin (logo)
Doctor Series
(circular pattern - Doctor Formulated, Registered Pharmacy, Handmade, Highest Medical Standards)
(Lid Balm No.5 - in hand writing and different color, maybe red)
Key Ingredients: (Marigold, Retinol - in hand writing, same color as above, maybe red)
(box with hand writing 30) ml
Lower Bottom Label (underneath surface of the container)
Made for Velluto Skin by
Pharmacy Lorant, 7 Pelister blvd., Sofia, ph. 0893517460
Patient: (Teodora Halvik- in hand writing)
Pharmacist: (Signature - in hand writing)
Date: (01.01.2017 - in hand writing)
For External Use
good for 60 days after preparation
Ingredients: Retinol, Marigold Extract, Water, Glycerin, Stearyl Alcohol, Wheat Germ Oil, Polysorbate 60, Sesame Oil, Myristyl Myristate, Cetyl Alcohol, Sorbitan Stearate, Phenoxyethanol, Calendula Extract, Cornflower Extract, Sodium Alginate, Sodium Citrate.
The container lid and bottom are 5 cm = 50 mm in diameter. Made from aluminum and contain 30ml or 50ml.
Please refer to the screen shots from my Web Site to get the feeling for the color pallet and professional look. These creams will be sold on this website. They are custom made by a registered Pharmacy right on the spot after the order has been placed. This is why I need more space for the hand written notes made by the pharmacist who prepared the order.
Please make the design professional, simple and serious colors, like light brown, beige, black or dark brown letters, red hand writing (will be filled by pen or thin marker by the Pharmacist by hand, depending on the order, patient name, etc.)
Thank you.
female 24 - 49 year old
Medical

```html
<!DOCTYPE html>
<html lang="en">
<head>
<meta charset="utf-8">
<title>Velluto Skin – Bottom Label</title>
<link href="https://fonts.googleapis.com/css2?family=Poiret+One&display=swap" rel="stylesheet">
<style>
  :root {
    --paper: #ffffff;
    --rim: #8a8a8a;
    --dots: #7a7a7a;
    --ink-strong: #3a3a3a;
    --ink-mid: #a9a9a9;
    --ink-soft: #cfcfcf;
    --rule: #3a3a3a;
  }
  html, body {
    margin: 0;
    padding: 0;
    width: 1200px;
    height: 1200px;
    overflow: hidden;
    background: var(--paper);
  }
  .label {
    display: block;
    width: 1200px;
    height: 1200px;
    font-family: "Poiret One", sans-serif;
  }
  .label__rim {
    fill: none;
    stroke: var(--rim);
    stroke-width: 2;
  }
  .label__dotted-ring {
    fill: none;
    stroke: var(--dots);
    stroke-width: 5;
    stroke-linecap: round;
    stroke-dasharray: 0 10.3;
  }
  .maker {
    fill: var(--ink-soft);
    font-size: 36px;
    text-anchor: middle;
  }
  .field-label {
    fill: var(--ink-strong);
    font-size: 44px;
    text-anchor: end;
  }
  .field-rule {
    stroke: var(--rule);
    stroke-width: 2;
  }
  .usage {
    fill: var(--ink-mid);
    font-size: 28px;
    text-anchor: middle;
  }
  .ingredients {
    fill: var(--ink-soft);
    font-size: 30px;
    text-anchor: middle;
  }
</style>
</head>
<body>
<svg class="label" viewBox="0 0 1200 1200" xmlns="http://www.w3.org/2000/svg">
  <circle class="label__rim" cx="600" cy="600" r="596"/>
  <circle class="label__dotted-ring" cx="600" cy="600" r="494"/>

  <g class="maker-block">
    <text class="maker" x="600" y="258">Made for Velluto Skin by</text>
    <text class="maker" x="600" y="308">Pharmacy Lorant, 7 Pelister blvd.,</text>
    <text class="maker" x="600" y="356">Sofia, ph. 0893517460</text>
  </g>

  <g class="fields">
    <text class="field-label" x="400" y="460">Patient:</text>
    <line class="field-rule" x1="400" y1="464" x2="868" y2="464"/>
    <text class="field-label" x="400" y="528">Date:</text>
    <line class="field-rule" x1="400" y1="532" x2="868" y2="532"/>
    <text class="field-label" x="400" y="598">Pharmacist:</text>
    <line class="field-rule" x1="400" y1="600" x2="868" y2="600"/>
  </g>

  <g class="usage-block">
    <text class="usage" x="600" y="666">For External Use</text>
    <text class="usage" x="600" y="719">good for 60 days after preparation</text>
  </g>

  <g class="ingredient-list">
    <text class="ingredients" x="600" y="784">Ingredients: Retinol, Marigold Extract, Water, Glycerin,</text>
    <text class="ingredients" x="600" y="826">Stearyl Alcohol, Wheat Germ Oil, Polysorbate 60,</text>
    <text class="ingredients" x="600" y="868">Sesame Oil, Myristyl Myristate, Cetyl Alcohol,</text>
    <text class="ingredients" x="600" y="910">Sorbitan Stearate, Phenoxyethanol,</text>
    <text class="ingredients" x="600" y="952">Calendula Extract, Cornflower Extract,</text>
    <text class="ingredients" x="600" y="994">Sodium Alginate, Sodium Citrate.</text>
  </g>
</svg>
</body>
</html>
```